dog treat packaging

packaging for dog treat brand named Tolliver
below images of whsat the packages will look like / please post designs on same packaging

Industry/Entity Type

Pet

Requirements
Must have
• funky / cool /fun / unique / playful

```html
<!DOCTYPE html>
<html lang="en">
<head>
<meta charset="utf-8">
<title>Tolliver Chicken Bites – Pouch</title>
<link rel="stylesheet" href="https://fonts.googleapis.com/css2?family=Lilita+One&family=Nunito:wght@600;700&family=Roboto+Slab:wght@400&display=swap">
<style>
  :root {
    --backdrop: #ffffff;
    --pouch-cream: #f4ecd5;
    --pouch-cream-light: #faf5e6;
    --sky-blue: #2cb4e4;
    --sun-orange: #f5b13a;
    --label-orange: #f8c45e;
    --ink-dark: #2a2a2a;
    --bite-brown: #7a3a12;
    --logo-blue: #29a6dc;
    --white: #ffffff;
  }
  * { margin: 0; padding: 0; box-sizing: border-box; }
  html, body { width: 1200px; height: 1200px; overflow: hidden; background: var(--backdrop); }
  .canvas { position: relative; width: 1200px; height: 1200px; overflow: hidden; }
  .pouch-art { position: absolute; inset: 0; width: 1200px; height: 1200px; }

  .tear-note {
    position: absolute; top: 160px; left: 0; width: 1270px; text-align: center;
    font: 600 22px/1 "Nunito", sans-serif; color: var(--ink-dark);
  }
  .brand-name {
    position: absolute; top: 230px; left: 100px; width: 580px; height: 64px;
    display: flex; align-items: center; justify-content: center; gap: 16px;
    font: 400 50px/1 "Lilita One", sans-serif; color: var(--logo-blue); letter-spacing: 1px;
  }
  .brand-dot { width: 30px; height: 30px; border-radius: 50%; background: var(--logo-blue); }

  .tagline {
    position: absolute; top: 344px; left: 186px;
    font: 600 26px/32px "Nunito", sans-serif; color: var(--ink-dark);
  }
  .dog-portrait {
    position: absolute; top: 450px; left: 228px; width: 690px; height: 270px;
    border: 5px solid var(--sun-orange); border-radius: 70px 90px 40px 40px;
    background: linear-gradient(120deg, #fdfbf5 0%, #e9d3b6 45%, #c79a72 70%, #f5f1ea 100%);
  }
  .flavour-label {
    position: absolute; top: 756px; left: 432px; width: 336px; height: 104px;
    border-radius: 18px; background: var(--label-orange);
    display: flex; flex-direction: column; align-items: center; justify-content: center;
    font: 400 34px/38px "Lilita One", sans-serif; color: var(--bite-brown); letter-spacing: 1px;
  }
  .claim {
    position: absolute; top: 1088px; left: 250px; width: 540px; text-align: center;
    font: 400 34px/37px "Roboto Slab", serif; color: var(--ink-dark);
  }
  .claim-strong { text-transform: uppercase; }
</style>
</head>
<body>
<main class="canvas">
  <svg class="pouch-art" viewBox="0 0 500 500" aria-hidden="false">
    <defs>
      <linearGradient id="pouchFill" x1="0" y1="0" x2="1" y2="1">
        <stop offset="0" stop-color="#faf5e6"/>
        <stop offset="1" stop-color="#efe4c8"/>
      </linearGradient>
      <linearGradient id="treatFill" x1="0" y1="0" x2="1" y2="1">
        <stop offset="0" stop-color="#e2a38c"/>
        <stop offset="0.5" stop-color="#c97a5f"/>
        <stop offset="1" stop-color="#b56a50"/>
      </linearGradient>
    </defs>
    <!-- pouch body with side tear notches -->
    <path class="pouch-body" fill="url(#pouchFill)"
      d="M22,0 H478 V40 L470,45 L478,50 V500 H22 V50 L30,45 L22,40 Z"/>
    <ellipse class="hang-hole" cx="250" cy="22" rx="30" ry="6" fill="#ffffff"/>
    <!-- blue side wave -->
    <path class="side-wave" fill="var(--sky-blue)"
      d="M478,85 C420,85 345,100 345,165 C345,230 385,255 365,300 C340,350 335,400 400,412 L478,412 Z"/>
    <!-- brand banner -->
    <path class="brand-banner" fill="var(--sun-orange)"
      d="M22,88 H270 A21,21 0 0 1 270,130 H22 Z"/>
    <rect class="brand-plate" x="40" y="95" width="245" height="28" rx="14" fill="#ffffff"/>
    <!-- bone window with treats -->
    <g role="img" aria-label="Photo of chicken breast treat bites seen through a bone-shaped window">
      <path fill="url(#treatFill)" stroke="var(--sun-orange)" stroke-width="3"
        d="M82,368 L353,368 A28,28 0 1 1 385,400 A28,28 0 1 1 353,432 L82,432 A28,28 0 1 1 50,400 A28,28 0 1 1 82,368 Z"/>
    </g>
  </svg>

  <p class="tear-note">Tear me to openand re-seal me for freshness!</p>

  <div class="brand-name"><span class="brand-dot"></span>TOLLIVER</div>

  <p class="tagline">Loved by<br>puppies and<br>small dogs</p>

  <div class="dog-portrait" role="img" aria-label="Four small dogs dressed in little outfits and crowns"></div>

  <div class="flavour-label"><span>CHICKEN</span><span>BITES</span></div>

  <p class="claim">With over 50%<br><span class="claim-strong">Natural Chicken</span><br>breast meat</p>
</main>
</body>
</html>
```